6 - 8 'Holistic' Instagram Graphics

Hi there!
We are looking to build up a library of Graphic Templates to use as Instagram & Facebook posts for our Holistic Medi Spa (& 3 other companies eventually)
This competition is for a sample of 6 - 8 designs. For the winner(s), we will make an agreement for a batch order (Looking for 200+ designs in total), and will be looking to make a long term arrangement.
Please find a full job description in the attached Word Document.
Any questions, don't hesitate to ask.
Thanks!
Medical Spa

```html
<!DOCTYPE html>
<html lang="en">
<head>
<meta charset="utf-8">
<title>Daytime Skincare Routine</title>
<link rel="stylesheet" href="https://fonts.googleapis.com/css2?family=Abril+Fatface&family=Open+Sans:wght@300&display=swap">
<style>
  :root {
    --mint: #eaf8f5;
    --sand: #f6eadf;
    --tan: #d8c2a0;
    --ink: #7f8074;
    --ink-soft: #8a8b82;
    --photo-light: #e4e4e4;
    --photo-mid: #d9c2b4;
  }
  html, body {
    margin: 0;
    padding: 0;
    width: 1200px;
    height: 1200px;
    overflow: hidden;
  }
  .post {
    position: relative;
    width: 1200px;
    height: 1200px;
    background: var(--mint);
    overflow: hidden;
  }
  .side-panel {
    position: absolute;
    top: 0;
    left: 802px;
    width: 398px;
    height: 1200px;
    background: var(--sand);
  }
  .leaf-sprig {
    position: absolute;
    left: 822px;
    top: 0;
    width: 236px;
    height: 328px;
    border-radius: 0 0 118px 118px;
    background: linear-gradient(160deg, var(--tan) 0%, var(--sand) 90%);
    opacity: 0.6;
  }
  .corner-ornament {
    position: absolute;
    left: 0;
    top: 753px;
    width: 142px;
    height: 447px;
    border-radius: 0 71px 0 0;
    background: var(--tan);
    opacity: 0.85;
  }
  .photo {
    position: absolute;
    left: 522px;
    top: 337px;
    width: 558px;
    height: 799px;
    border-top-left-radius: 380px 420px;
    background: linear-gradient(135deg, var(--photo-light) 0%, var(--photo-light) 45%, var(--photo-mid) 100%);
  }
  .title {
    position: absolute;
    left: 121px;
    top: 110px;
    margin: 0;
    font-family: "Abril Fatface", serif;
    font-weight: 400;
    font-size: 70px;
    line-height: 94px;
    color: var(--ink);
    letter-spacing: 1.5px;
  }
  .steps {
    position: absolute;
    left: 120px;
    top: 356px;
    margin: 0;
    padding: 0;
    list-style: none;
  }
  .step {
    display: flex;
    align-items: center;
    height: 74px;
    font-family: "Open Sans", sans-serif;
    font-weight: 300;
    font-size: 39px;
    color: var(--ink-soft);
    white-space: nowrap;
  }
  .step-tick {
    width: 52px;
    height: 44px;
    margin-right: 22px;
    flex: none;
  }
</style>
</head>
<body>
<main class="post">
  <div class="side-panel"></div>
  <div class="leaf-sprig" role="img" aria-label="Decorative leaf sprig in sand and mint tones"></div>
  <div class="corner-ornament" role="img" aria-label="Decorative organic sand-coloured shape"></div>

  <div class="photo" role="img" aria-label="Photo of a woman applying white face cream while holding an open jar"></div>

  <h1 class="title">Daytime<br>Skincare Routine</h1>

  <ul class="steps">
    <li class="step"><svg class="step-tick" viewBox="0 0 54 46" aria-hidden="true"><path d="M4 26 L20 41 L50 5" fill="none" stroke="var(--ink)" stroke-width="7" stroke-linecap="round" stroke-linejoin="round"/></svg>Cleanse</li>
    <li class="step"><svg class="step-tick" viewBox="0 0 54 46" aria-hidden="true"><path d="M4 26 L20 41 L50 5" fill="none" stroke="var(--ink)" stroke-width="7" stroke-linecap="round" stroke-linejoin="round"/></svg>Tone</li>
    <li class="step"><svg class="step-tick" viewBox="0 0 54 46" aria-hidden="true"><path d="M4 26 L20 41 L50 5" fill="none" stroke="var(--ink)" stroke-width="7" stroke-linecap="round" stroke-linejoin="round"/></svg>Vitamin C Serum</li>
    <li class="step"><svg class="step-tick" viewBox="0 0 54 46" aria-hidden="true"><path d="M4 26 L20 41 L50 5" fill="none" stroke="var(--ink)" stroke-width="7" stroke-linecap="round" stroke-linejoin="round"/></svg>Eye Cream</li>
    <li class="step"><svg class="step-tick" viewBox="0 0 54 46" aria-hidden="true"><path d="M4 26 L20 41 L50 5" fill="none" stroke="var(--ink)" stroke-width="7" stroke-linecap="round" stroke-linejoin="round"/></svg>Moisturizer</li>
  </ul>
</main>
</body>
</html>
```